brochure for high-end senior living company

We need a new brochure that we can pass out to doctors and social workers so they would choose us over the competition.
brightmeadowhaven.example is our website that shows our colors and themes

we stand out over our competition due to our high quality of staff and our staff to resident ratio.
We are not afraid of difficult and complex care situations. Instead, we thrive on coordinating complexity.

We do all of this in a lovely setting that is luxurious and feels like home.

Target Market(s)

The families who make the decision are 60-70 years old. They are not not "rich" but they have saved well and usually have more than 1 million in assets.

Industry/Entity Type

Senior Living, Memory Care

Font styles to use
Serif

Colors
00AB8E
00BBA5
67D7C9
C6EFE9
E9F9F6
FFC000
F8CF3A
FAE287
FDF2CF
FEFAEE

Requirements
Must have
• When compromise is not an option...
Nice to have
• A difficult balance of beautiful and activities (happy people), but also communicating that we handle difficult and complex care.

```html
<!DOCTYPE html>
<html lang="en">
<head>
<meta charset="utf-8">
<title>Bright Meadow Haven – Trifold Brochure</title>
<link href="https://fonts.googleapis.com/css2?family=Adamina&family=Marcellus&family=Catamaran:wght@400;500;600;800&display=swap" rel="stylesheet">
<style>
:root{
  --backdrop:#a7a7a7;
  --teal:#00AB8E;
  --teal-bright:#00BBA5;
  --teal-soft:#67D7C9;
  --teal-pale:#C6EFE9;
  --teal-mist:#E9F9F6;
  --teal-ink:#0a4a42;
  --gold:#FFC000;
  --gold-warm:#F8CF3A;
  --gold-light:#FAE287;
  --gold-pale:#FDF2CF;
  --cream:#FEFAEE;
  --gold-text:#d99e00;
  --ink:#1d2a29;
  --paper:#ffffff;
}
*{box-sizing:border-box;margin:0;padding:0}
html,body{width:1096px;height:1200px;overflow:hidden;background:var(--backdrop)}
body{position:relative;font-family:"Catamaran",Arial,sans-serif;color:var(--ink)}
.sheet{position:absolute;left:213px;width:669px;height:517px;background:var(--paper);overflow:hidden}
.sheet--outside{top:65px}
.sheet--inside{top:618px}
.sheet-art{position:absolute;left:0;top:0;width:669px;height:517px}
.block{position:absolute}
.serif-head{font-family:"Adamina",Georgia,serif;color:var(--gold-text);letter-spacing:.3px}
.serif-sub{font-family:"Adamina",Georgia,serif;color:var(--teal-ink)}
.lead{font-weight:600;font-size:8.6px;line-height:10.6px;color:var(--teal-ink)}
.body{font-size:7.6px;line-height:9.65px;text-align:justify;color:var(--ink)}
.body--light{color:#ffffff}
.sans-head{font-weight:800;color:var(--gold-pale);font-size:12px;line-height:14px}

/* about panel */
.about{left:24px;top:18px;width:176px}
.about .serif-head{font-size:16px;margin-bottom:9px}
.about .serif-sub{font-size:11.2px;line-height:14.5px;margin-bottom:10px}
.about .gap{height:20px}

/* reasons panel */
.reasons-title{left:248px;top:20px;font-weight:800;color:var(--gold-pale);font-size:11.4px;line-height:14px}
.reason{position:absolute;left:281px;font-size:8px;line-height:10px;color:#fff;font-weight:500}
.brand-mid{left:223px;top:262px;width:224px;text-align:center}
.brand-name{font-family:"Marcellus",Georgia,serif;color:#fff;font-size:14.5px;letter-spacing:.6px;line-height:18px;white-space:nowrap}
.brand-line{font-family:"Marcellus",Georgia,serif;color:#fff;font-size:11.2px;line-height:14px;margin-top:3px}
.contact{left:223px;top:320px;width:224px;text-align:center;color:#fff}
.contact h3{font-weight:800;color:var(--gold-pale);font-size:11.4px;line-height:14px;margin-bottom:3px}
.contact .ico{display:block;margin:0 auto 2px}
.contact p{font-size:9.6px;line-height:12.4px;font-weight:500;margin-bottom:5px}

/* cover panel */
.cover{left:447px;top:318px;width:222px;text-align:center}
.cover .brand-name{color:var(--teal-ink);font-size:15.5px;line-height:19px}
.cover .brand-line{color:var(--teal-ink);font-size:12px;line-height:15px}
.promise{font-family:"Adamina",Georgia,serif;color:var(--gold-text);font-size:10.4px;line-height:13px;margin-top:12px}
.tagline{font-family:"Adamina",Georgia,serif;color:var(--teal-ink);font-size:15.5px;line-height:18px;margin-top:6px}
.cover-badge{margin:8px auto 0;width:175px;height:45px;background:var(--gold);color:var(--teal-ink);font-weight:600;font-size:11.2px;line-height:15px;display:flex;align-items:center;justify-content:center;text-align:center}
.cover-web{margin-top:8px;font-weight:600;font-size:10.6px;color:var(--ink)}

/* inside */
.what{left:24px;top:21px;width:176px}
.what .sans-head{margin-bottom:3px}
.what .gap{height:19px}
.services-title{left:247px;top:334px;font-family:"Adamina",Georgia,serif;font-size:16px;color:var(--teal-ink);letter-spacing:.3px}
.service{position:absolute;font-size:8.6px;line-height:10.4px;font-weight:500;color:var(--ink)}
.facility{left:470px;top:303px;width:174px}
.facility .serif-sub{font-size:10.4px;margin-bottom:9px;white-space:nowrap}
.facility .lead{font-size:9.2px;line-height:11px;font-weight:500;margin-bottom:4px}
</style>
</head>
<body>

<section class="sheet sheet--outside">
  <svg class="sheet-art" viewBox="0 0 669 517">
    <defs>
      <linearGradient id="gardenTone" x1="0" y1="0" x2="1" y2="1">
        <stop offset="0" stop-color="#8b8a6c"/><stop offset=".5" stop-color="#6f7a4c"/><stop offset="1" stop-color="#c7b79a"/>
      </linearGradient>
      <linearGradient id="roomTone" x1="0" y1="0" x2="1" y2="1">
        <stop offset="0" stop-color="#cfc0a8"/><stop offset=".5" stop-color="#b89a72"/><stop offset="1" stop-color="#6e5a4e"/>
      </linearGradient>
      <linearGradient id="tableTone" x1="0" y1="0" x2="1" y2="1">
        <stop offset="0" stop-color="#a7b59a"/><stop offset="1" stop-color="#5f6e5a"/>
      </linearGradient>
      <linearGradient id="houseTone" x1="0" y1="0" x2="0" y2="1">
        <stop offset="0" stop-color="#00AB8E"/><stop offset="1" stop-color="#00907a"/>
      </linearGradient>
      <linearGradient id="paperFold" x1="0" y1="0" x2="1" y2="0">
        <stop offset="0" stop-color="#E9F9F6"/><stop offset=".18" stop-color="#ffffff"/>
      </linearGradient>
    </defs>
    <rect x="0" y="0" width="223" height="517" fill="url(#paperFold)"/>
    <rect x="447" y="0" width="222" height="517" fill="url(#paperFold)"/>
    <rect x="223" y="0" width="224" height="517" fill="var(--teal)"/>

    <g role="img" aria-label="Photo: caregiver pushing a smiling senior man in a wheelchair along a garden path">
      <path d="M398 0 H669 V286 C600 296 520 292 470 270 C430 250 405 200 398 0 Z" fill="url(#gardenTone)"/>
    </g>
    <path d="M455 268 C520 302 610 300 669 288" fill="none" stroke="var(--gold)" stroke-width="4"/>

    <g role="img" aria-label="Photo: caregiver with a senior man enjoying a meal">
      <circle cx="400" cy="63" r="50" fill="url(#roomTone)" stroke="var(--gold)" stroke-width="5"/>
    </g>
    <g role="img" aria-label="Photo: residents dining together at an outdoor patio table">
      <circle cx="427" cy="197" r="54" fill="url(#tableTone)" stroke="var(--gold)" stroke-width="5"/>
    </g>

    <line x1="263" y1="84" x2="263" y2="188" stroke="var(--gold-light)" stroke-width=".8" stroke-dasharray="1.5 2"/>
    <g fill="none" stroke="var(--gold-light)" stroke-width="1.4">
      <circle cx="263" cy="71" r="12.5"/><circle cx="263" cy="71" r="10"/>
      <circle cx="263" cy="114" r="12.5"/><circle cx="263" cy="114" r="10"/>
      <circle cx="263" cy="158" r="12.5"/><circle cx="263" cy="158" r="10"/>
      <circle cx="263" cy="201" r="12.5"/><circle cx="263" cy="201" r="10"/>
    </g>
    <g fill="none" stroke="#fff" stroke-width=".9">
      <rect x="257" y="68" width="12" height="5"/><line x1="257" y1="73" x2="257" y2="76"/><line x1="269" y1="73" x2="269" y2="76"/>
      <path d="M258 117 L268 111 M258 111 L268 117"/><circle cx="263" cy="110" r="2"/>
      <path d="M263 162 C256 157 257 152 260 152 C262 152 263 154 263 154 C263 154 264 152 266 152 C269 152 270 157 263 162 Z"/>
      <circle cx="263" cy="201" r="6"/><text x="263" y="203" font-size="4.5" fill="#fff" stroke="none" text-anchor="middle" font-family="Catamaran,sans-serif">24/7</text>
    </g>

    <g role="img" aria-label="Photo: caregiver dancing with a cheerful senior man in a living room">
      <path d="M0 352 C40 335 100 332 135 345 L195 410 C215 445 224 480 228 517 L0 517 Z" fill="url(#roomTone)"/>
    </g>
    <path d="M0 352 C40 335 100 332 135 345" fill="none" stroke="var(--gold)" stroke-width="5"/>
    <path d="M200 415 C216 448 224 482 228 517" fill="none" stroke="var(--gold)" stroke-width="4"/>
    <g role="img" aria-label="Photo: smiling resident holding oversized playing cards">
      <circle cx="171" cy="376" r="46" fill="#c9b9b3" stroke="var(--gold)" stroke-width="5"/>
    </g>

    <g role="img" aria-label="Faint photo of the residential home exterior">
      <rect x="228" y="447" width="219" height="70" fill="url(#houseTone)"/>
    </g>
  </svg>

  <div class="block about">
    <h2 class="serif-head">ABOUT US</h2>
    <h3 class="serif-sub">Learn More About Bright Meadow Haven Residential Assisted Living</h3>
    <p class="lead">Our Fairbrook and Willow Ridge Senior Caregivers are Compassionate &amp; Attentive</p>
    <p class="body">Though it may be obvious that Bright Meadow Haven takes care of older folks, what’s not as evident is how we do it. We have had many people drive up and down our street and call us saying “I can’t find your building, there’s just a bunch of houses here.” It’s so common in our society that the elderly are mainly served in institutional, commercial, apartment-like buildings. We are used to it and chuckle as we explain that indeed, they are on the right street.</p>
    <div class="gap"></div>
    <p class="lead">Exceptional Care, Safety &amp; Customer Service</p>
    <p class="body">Bright Meadow Haven was started by and is operated by me (Ravi) and I couldn’t do it without the help of my wife, Helen. We live locally in Fairbrook with our three little children: Nora, Owen, and Lily. We believe that every person, young and old, is created equal and deserves dignity. We believe that and set out to build a business that reflects that. The care, comfort, and happiness of our residents and their families is our daily pursuit.</p>
  </div>

  <div class="block reasons-title">REASONS<br>TO CHOOSE US</div>
  <div class="reason" style="top:62px">Private Rooms<br>&amp; Bathrooms</div>
  <div class="reason" style="top:100px">Delicious and<br>Healthy Home<br>Cooked Meals</div>
  <div class="reason" style="top:143px">Highest Caregiver to<br>Resident Ratio in the<br>Industry</div>
  <div class="reason" style="top:192px">24/7 Well-Trained<br>Caregivers on Site</div>

  <div class="block brand-mid">
    <div class="brand-name">BRIGHT MEADOW HAVEN</div>
    <div class="brand-line">Residential Assisted Living</div>
  </div>

  <div class="block contact">
    <h3>CONTACT US</h3>
    <svg class="ico" width="9" height="9" viewBox="0 0 10 10" aria-hidden="true"><circle cx="5" cy="5" r="5" fill="var(--gold)"/><path d="M5 2.2a1.9 1.9 0 0 1 1.9 1.9C6.9 5.5 5 7.8 5 7.8S3.1 5.5 3.1 4.1A1.9 1.9 0 0 1 5 2.2z" fill="var(--teal-ink)"/></svg>
    <p>4120 Linden Way<br>Fairbrook, CA 95000</p>
    <svg class="ico" width="9" height="9" viewBox="0 0 10 10" aria-hidden="true"><circle cx="5" cy="5" r="5" fill="var(--gold)"/><path d="M3.2 2.6l1 1-.5.8c.3.7.9 1.3 1.6 1.6l.8-.5 1 1-.7.9C4.6 7.2 2.8 5.4 2.6 3.3z" fill="var(--teal-ink)"/></svg>
    <p>555-214-0376</p>
    <svg class="ico" width="9" height="9" viewBox="0 0 10 10" aria-hidden="true"><circle cx="5" cy="5" r="5" fill="var(--gold)"/><g fill="none" stroke="var(--teal-ink)" stroke-width=".7"><circle cx="5" cy="5" r="2.8"/><ellipse cx="5" cy="5" rx="1.2" ry="2.8"/><line x1="2.2" y1="5" x2="7.8" y2="5"/></g></svg>
    <p>www.brightmeadowhaven.example</p>
  </div>

  <div class="block cover">
    <div class="brand-name">BRIGHT MEADOW HAVEN</div>
    <div class="brand-line">Residential Assisted Living</div>
    <p class="promise">When compromise is not an option...</p>
    <div class="tagline">The Perfect Balance of<br>Safety &amp; Warmth</div>
    <div class="cover-badge">Professional &amp; Friendly Care<br>in a Home Environment</div>
    <div class="cover-web">www.brightmeadowhaven.example</div>
  </div>
</section>

<section class="sheet sheet--inside">
  <svg class="sheet-art" viewBox="0 0 669 517">
    <defs>
      <linearGradient id="partyTone" x1="0" y1="0" x2="1" y2="1">
        <stop offset="0" stop-color="#c9c0b2"/><stop offset=".45" stop-color="#8a6e63"/><stop offset="1" stop-color="#b9a596"/>
      </linearGradient>
      <linearGradient id="yardTone" x1="0" y1="0" x2="1" y2="1">
        <stop offset="0" stop-color="#6f8a52"/><stop offset="1" stop-color="#b8b1a0"/>
      </linearGradient>
      <linearGradient id="paperFold2" x1="0" y1="0" x2="1" y2="0">
        <stop offset="0" stop-color="#E9F9F6"/><stop offset=".18" stop-color="#ffffff"/>
      </linearGradient>
    </defs>
    <rect x="0" y="0" width="223" height="517" fill="var(--teal)"/>
    <rect x="446" y="0" width="223" height="517" fill="url(#paperFold2)"/>
    <rect x="223" y="0" width="223" height="517" fill="#fff"/>

    <g role="img" aria-label="Photo: residents in festive masks toasting together around a dining table">
      <path d="M223 0 H669 V262 C600 274 520 286 440 294 C360 300 280 288 223 275 Z" fill="url(#partyTone)"/>
    </g>
    <path d="M440 294 C520 286 600 274 669 262" fill="none" stroke="var(--gold)" stroke-width="5"/>

    <g role="img" aria-label="Photo: caregiver playing a board game with a resident">
      <circle cx="296" cy="268" r="55" fill="#b5a08f" stroke="var(--gold)" stroke-width="6"/>
    </g>
    <g role="img" aria-label="Photo: musician playing the harp for residents">
      <circle cx="406" cy="268" r="55" fill="#c9b8a2" stroke="var(--gold)" stroke-width="6"/>
    </g>

    <g role="img" aria-label="Photo: residents with walkers visiting an ice cream truck outdoors">
      <path d="M0 345 C40 330 100 326 140 338 L198 400 C215 440 224 480 228 517 L0 517 Z" fill="url(#yardTone)"/>
    </g>
    <path d="M0 345 C40 330 100 326 140 338" fill="none" stroke="var(--gold)" stroke-width="5"/>
    <path d="M203 406 C217 444 224 482 228 517" fill="none" stroke="var(--gold)" stroke-width="4"/>
    <g role="img" aria-label="Photo: smiling resident in a white cardigan">
      <circle cx="163" cy="351" r="47" fill="#cfc4bb" stroke="var(--gold)" stroke-width="5"/>
    </g>

    <g fill="var(--teal)">
      <circle cx="262" cy="373" r="13"/><circle cx="368" cy="373" r="13"/>
      <circle cx="262" cy="410" r="13"/><circle cx="368" cy="410" r="13"/>
      <circle cx="262" cy="448" r="13"/><circle cx="368" cy="448" r="13"/>
      <circle cx="262" cy="485" r="13"/>
    </g>
    <g fill="none" stroke="var(--gold)" stroke-width="1">
      <circle cx="262" cy="373" r="11"/><circle cx="368" cy="373" r="11"/>
      <circle cx="262" cy="410" r="11"/><circle cx="368" cy="410" r="11"/>
      <circle cx="262" cy="448" r="11"/><circle cx="368" cy="448" r="11"/>
      <circle cx="262" cy="485" r="11"/>
    </g>
    <g fill="none" stroke="#fff" stroke-width=".9">
      <circle cx="262" cy="372" r="5"/>
      <path d="M364 369 L368 373 L372 369 M368 373 V378"/>
      <path d="M258 414 V406 M261 414 V405 M264 414 V405 M267 414 V407"/>
      <circle cx="368" cy="410" r="2"/><path d="M363 405 L366 408 M373 405 L370 408 M363 415 L366 412 M373 415 L370 412"/>
      <circle cx="262" cy="448" r="5.5"/><path d="M262 445 V448 H265"/>
      <path d="M362 446 C364 452 372 452 374 446"/><path d="M368 440 V446"/>
      <circle cx="262" cy="483" r="3"/><path d="M257 491 C257 487 267 487 267 491"/>
    </g>
  </svg>

  <div class="block what">
    <h2 class="sans-head">What We Do</h2>
    <p class="body body--light">In America, people aren’t used to assistance. We love independence and freedom and don’t plan on giving them up. At Bright Meadow Haven Residential Assisted Living, we get that. When a person comes through our doors and needs to transition to more assistance, we work very hard to make it painless and, dare we say, enjoyable! We come alongside strong independent people and offer gentle, patient, and friendly help.</p>
    <div class="gap"></div>
    <h2 class="sans-head">Why We Do What We Do</h2>
    <p class="body body--light">Being in assisted living such a long time, we saw the spectrum of care that exists out there. We saw a need for higher acuity care. So we set out to find the sweet balance of high quality care combined with a home atmosphere. We do that through a three-pronged method. First, we partner with licensed medical help every step of the way. Second, we hire CNAs, medical assistants, and nurses on their way to becoming registered. Third, we only choose homes that are spacious and inviting. We believe this balance accomplishes our pursuit of doing for our residents what we would like done for us.</p>
  </div>

  <h2 class="block services-title">OUR SERVICES</h2>
  <div class="service" style="left:282px;top:363px">Alzheimer’s &amp;<br>Dementia Care</div>
  <div class="service" style="left:388px;top:363px">Stroke<br>Care</div>
  <div class="service" style="left:282px;top:400px">Parkinson’s<br>Care</div>
  <div class="service" style="left:388px;top:400px">Limited<br>Mobility</div>
  <div class="service" style="left:282px;top:437px">Short Term<br>Stays</div>
  <div class="service" style="left:388px;top:437px">Hospice<br>Care</div>
  <div class="service" style="left:282px;top:474px">Skin &amp; Incontinence<br>Care</div>

  <div class="block facility">
    <h3 class="serif-sub">Fairbrook Assisted Living Facility</h3>
    <p class="lead">We’ll Treat Your Loved One Like Family:<br>555.214.0376</p>
    <p class="body">We at Bright Meadow Haven Residential Assisted Living realize that entrusting the health and well-being of your elderly loved one to an assisted living home is no easy decision. You want to find a home that will provide them with exceptional care in a beautiful and pleasant setting. Most assisted living homes look and feel institutional and sterile - but not ours. Our assisted living home looks like the other homes that line our residential street. We opened our doors with the purpose of providing the best combination of professional care and a comfortable home environment for seniors in Fairbrook. If you are seeking assisted living in Willow Ridge or Fairbrook, you can feel confident turning to Bright Meadow Haven Residential Assisted Living!</p>
  </div>
</section>

</body>
</html>
```